Page lark & Glimmerly ad needed

I am in need of a simple static image ad to be used for Pagelark & Glimmerly. A photo of a nice roof on a nice house. "Instant Satellite Roof Estimates" "Your house, your time & instant estimate" . Our logo file is here: https://www.filquarry.com/scl/fo/t52wqpzx73hmbnvekcy8d/ZKqWT5PLmNdbX3HfGsYe8r2?rlkey=vn7cz2ktbw94pqdr6yjmfx4cs&dl=0

Multiple variations will be purchased.

```html
<!DOCTYPE html>
<html lang="en">
<head>
<meta charset="utf-8">
<title>Hollowell Roofing – Instant Satellite Roof Estimates</title>
<link href="https://fonts.googleapis.com/css2?family=Arimo:wght@400;700&display=swap" rel="stylesheet">
<style>
  :root {
    --navy: #22374f;
    --navy-deep: #1c2f45;
    --gold: #ecb953;
    --white: #ffffff;
    --paper: #ececec;
    --stripe: #e2e2e2;
  }
  * { box-sizing: border-box; margin: 0; padding: 0; }
  html, body { width: 1199px; height: 1200px; overflow: hidden; background: var(--paper); }
  .ad {
    position: relative; width: 1199px; height: 1200px; overflow: hidden;
    font-family: "Arimo", Arial, sans-serif;
    background: repeating-linear-gradient(135deg, var(--paper) 0 6px, var(--stripe) 6px 7px);
  }
  .backdrop { position: absolute; inset: 0; }
  .tech-tag {
    position: absolute; top: 0; right: 0; width: 180px; height: 79px;
    background: var(--gold); border-bottom-left-radius: 25px;
    padding: 19px 0 0 35px;
    color: var(--navy); font-weight: 700; font-size: 16px; line-height: 23px;
    box-shadow: 0 6px 18px rgba(0,0,0,.2);
  }
  .brand {
    position: absolute; top: 92px; left: 0; width: 1199px; text-align: center;
    color: var(--white); font-weight: 700; font-size: 20px; line-height: 22px; letter-spacing: 1px;
  }
  .brand-mark { display: inline-block; width: 10px; height: 10px; background: var(--white); margin-right: 8px; vertical-align: 2px; }
  .headline-band {
    position: absolute; display: flex; align-items: center; justify-content: center;
    box-shadow: 0 10px 20px rgba(0,0,0,.25);
  }
  .band-satellite { left: 225px; top: 237px; width: 750px; height: 94px; background: var(--gold); transform: rotate(-2deg); }
  .band-estimates { left: 366px; top: 441px; width: 467px; height: 93px; background: var(--white); transform: rotate(2deg); }
  .band-text {
    color: var(--navy); font-weight: 700; display: inline-block; transform: scaleY(1.22);
    line-height: 1; letter-spacing: 0;
  }
  .band-satellite .band-text { font-size: 66px; margin-top: 6px; }
  .band-estimates .band-text { font-size: 64px; margin-top: -4px; }
  .headline-roof {
    position: absolute; top: 346px; left: 0; width: 1199px; text-align: center;
    font-size: 79px; font-weight: 700; line-height: 1;
    background: linear-gradient(180deg, #ffffff 40%, #cfd3d8 100%);
    -webkit-background-clip: text; background-clip: text; color: transparent;
  }
  .tagline {
    position: absolute; top: 554px; left: 0; width: 1199px; text-align: center;
    color: var(--white); font-size: 27px; line-height: 32px;
  }
  .photo-card { position: absolute; top: 626px; width: 373px; height: 373px; }
  .card-back { position: absolute; inset: 0; border-radius: 18px; }
  .card-front { position: absolute; inset: 0; border-radius: 18px; border: 5px solid var(--white); overflow: hidden; }
  .card-framing { left: 26px; }
  .card-framing .card-back { background: var(--gold); transform: rotate(3deg) translate(-6px, 4px); }
  .card-aerial { left: 413px; }
  .card-aerial .card-back { background: var(--white); transform: rotate(-2.5deg); }
  .card-aerial .card-front { border-color: var(--gold); }
  .card-battens { left: 799px; }
  .card-battens .card-back { background: var(--navy-deep); transform: rotate(2.5deg) translate(4px, 4px); }
  .photo { width: 100%; height: 100%; }
  .photo-framing { background: linear-gradient(165deg, #2f73c2 0%, #6d9bd4 38%, #e9dcc1 62%, #c7ae7c 100%); }
  .photo-aerial { background: radial-gradient(ellipse at 50% 50%, #d8c39a 0%, #bfae8c 35%, #a79f86 55%, #5e7a48 85%); }
  .photo-battens { background: linear-gradient(200deg, #5f86cd 0%, #8cabd9 28%, #c9b895 50%, #6f7680 80%, #2e7a62 100%); }
  .cta {
    position: absolute; left: 26px; top: 1019px; width: 1146px; height: 77px;
    border-radius: 39px; background: var(--gold); border: 4px solid var(--navy);
    display: flex; align-items: center; justify-content: center;
    color: var(--navy); font-weight: 700; font-size: 26px; letter-spacing: .3px;
  }
  .contact-bar {
    position: absolute; left: 26px; top: 1112px; width: 1146px; height: 60px;
    background: var(--white); border-radius: 12px; box-shadow: 0 4px 14px rgba(0,0,0,.08);
    display: flex; align-items: center; justify-content: center; gap: 36px;
  }
  .contact-item { display: flex; align-items: center; gap: 10px; color: var(--navy); font-weight: 700; font-size: 16px; }
  .contact-icon { width: 36px; height: 36px; border-radius: 50%; display: flex; align-items: center; justify-content: center; }
  .icon-web { background: var(--gold); }
  .icon-phone { background: var(--navy); }
</style>
</head>
<body>
<main class="ad">
  <svg class="backdrop" width="1199" height="1200" viewBox="0 0 1199 1200" aria-hidden="true">
    <polygon points="0,0 1199,0 1199,838 0,1019" fill="var(--navy)"/>
  </svg>

  <div class="tech-tag">SATELLITE<br>TECHNOLOGY</div>

  <div class="brand"><span class="brand-mark"></span>HOLLOWELL ROOFING</div>

  <div class="headline-band band-satellite"><span class="band-text">INSTANT SATELLITE</span></div>
  <h1 class="headline-roof">ROOF</h1>
  <div class="headline-band band-estimates"><span class="band-text">ESTIMATES</span></div>

  <p class="tagline">Your house, your time &amp; instant estimate</p>

  <div class="photo-card card-framing">
    <div class="card-back"></div>
    <div class="card-front"><div class="photo photo-framing" role="img" aria-label="Wooden roof trusses against a blue sky"></div></div>
  </div>
  <div class="photo-card card-aerial">
    <div class="card-back"></div>
    <div class="card-front"><div class="photo photo-aerial" role="img" aria-label="Aerial view of a house under construction with plywood roof decking"></div></div>
  </div>
  <div class="photo-card card-battens">
    <div class="card-back"></div>
    <div class="card-front"><div class="photo photo-battens" role="img" aria-label="Roofers installing wooden battens on a pitched roof"></div></div>
  </div>

  <div class="cta">GET STARTED</div>

  <div class="contact-bar">
    <div class="contact-item">
      <span class="contact-icon icon-web">
        <svg width="16" height="16" viewBox="0 0 16 16" aria-hidden="true" fill="none" stroke="var(--navy)" stroke-width="1.6">
          <circle cx="8" cy="8" r="6.5"/><ellipse cx="8" cy="8" rx="2.8" ry="6.5"/><line x1="1.5" y1="8" x2="14.5" y2="8"/>
        </svg>
      </span>
      hollowellroofing.com
    </div>
    <div class="contact-item">
      <span class="contact-icon icon-phone">
        <svg width="16" height="16" viewBox="0 0 24 24" aria-hidden="true" fill="var(--gold)">
          <path d="M6.6 10.8a15.1 15.1 0 0 0 6.6 6.6l2.2-2.2a1 1 0 0 1 1-.25 11.4 11.4 0 0 0 3.6.57 1 1 0 0 1 1 1V20a1 1 0 0 1-1 1A17 17 0 0 1 3 4a1 1 0 0 1 1-1h3.5a1 1 0 0 1 1 1c0 1.25.2 2.45.57 3.57a1 1 0 0 1-.25 1z"/>
        </svg>
      </span>
      (555) 238-9104
    </div>
  </div>
</main>
</body>
</html>
```